Business card design needed

Double sided
Color, unique, elegant

Maybe put this quote somewhere?? But I think it might make it to cluttered?
“The Hartwick Method of Body
Conditioning develops the body
uniformly, corrects posture, restores
vitality, invigorates the mind and
elevates the spirit”
- Lionel Hartwick

Industry/Entity Type

Business

Contact Information for Business Card

Marla Trevisick
Pilates Instructor & Personal trainer
Mobile: 0498260543
www.kovira.com.au
email: koviraheal.motion@brintmail.com

```html
<!DOCTYPE html>
<html lang="en">
<head>
<meta charset="utf-8">
<title>Kovira Health and Fitness – Business Card</title>
<link rel="stylesheet" href="https://fonts.googleapis.com/css2?family=Poiret+One&family=Questrial&display=swap">
<style>
  :root {
    --sage: #c2ccbf;
    --blush: #e9bde6;
    --orchid: #c963bf;
    --mint: #c6efc8;
    --leaf: #77d97e;
    --ink: #111111;
    --forest: #2f5a35;
    --mist-light: #f0f0f0;
    --mist-mid: #c4c4c4;
    --mist-dark: #9a9a9a;
  }
  * { margin: 0; padding: 0; box-sizing: border-box; }
  html, body {
    width: 1200px;
    height: 686px;
    overflow: hidden;
    background: #ffffff;
  }
  .card {
    position: relative;
    width: 1200px;
    height: 686px;
    overflow: hidden;
  }
  .corner-block {
    position: absolute;
    left: 0; top: 0;
    width: 141px; height: 109px;
    background: var(--sage);
  }
  .side-panel {
    position: absolute;
    left: 0; top: 149px;
    width: 141px; height: 537px;
    background: var(--blush);
  }
  .header-band {
    position: absolute;
    left: 141px; top: 0;
    width: 1059px; height: 109px;
    background: var(--mint);
  }
  .accent-band {
    position: absolute;
    left: 0; top: 109px;
    width: 1200px; height: 40px;
    background: var(--leaf);
  }
  .accent-stripe {
    position: absolute;
    left: 141px; top: 0;
    width: 40px; height: 686px;
    background: var(--orchid);
  }
  .backdrop {
    position: absolute;
    left: 181px; top: 149px;
    width: 1019px; height: 537px;
    background:
      radial-gradient(ellipse at 45% 55%, var(--mist-light) 0%, rgba(240,240,240,0) 65%),
      linear-gradient(200deg, var(--mist-dark) 0%, var(--mist-mid) 35%, var(--mist-light) 65%, var(--mist-mid) 100%);
  }
  .brand-name {
    position: absolute;
    left: 208px; top: 2px;
    font-family: "Poiret One", sans-serif;
    font-weight: 400;
    font-size: 92px;
    letter-spacing: 4px;
    color: var(--forest);
    text-transform: uppercase;
    line-height: 1;
  }
  .brand-tagline {
    position: absolute;
    left: 569px; top: 70px;
    font-family: "Questrial", sans-serif;
    font-size: 36px;
    letter-spacing: 0.5px;
    color: var(--forest);
    line-height: 1;
    white-space: nowrap;
  }
  .quote {
    position: absolute;
    left: 194px; top: 150px;
    font-family: "Poiret One", sans-serif;
    font-size: 48px;
    font-weight: 400;
    text-transform: uppercase;
    letter-spacing: 1px;
    line-height: 55px;
    color: var(--ink);
    white-space: nowrap;
  }
  .quote-author {
    position: absolute;
    left: 194px; top: 534px;
    font-family: "Poiret One", sans-serif;
    font-size: 48px;
    text-transform: uppercase;
    letter-spacing: 1px;
    line-height: 55px;
    color: var(--ink);
    white-space: nowrap;
  }
</style>
</head>
<body>
  <main class="card">
    <div class="corner-block"></div>
    <div class="side-panel"></div>
    <div class="header-band"></div>
    <div class="accent-band"></div>
    <div class="backdrop" role="img" aria-label="Soft grey photograph of raindrops on a misty window"></div>
    <div class="accent-stripe"></div>

    <h1 class="brand-name">Kovira</h1>
    <p class="brand-tagline">Health and Fitness</p>

    <blockquote class="quote">
      “The Hartwick Method of Body<br>
      Conditioning builds the body<br>
      evenly, improves balance and form,<br>
      renews<br>
      energy, steadies the mind and<br>
      lifts the spirit”
    </blockquote>
    <p class="quote-author">- Lionel Hartwick</p>
  </main>
</body>
</html>
```